Biz Card Design TPVC

New business card for a new company.
Logo was completed by a designer on ArtFlock and looking to continue requesting additional services.
Company Name: Tidal Prime Voltage Collective
Although this company is starting in Canada, we will be moving towards a global presence within the next 6 months.
Key elements to this business are as follows.
Energy Procurement
Energy Reduction Services
Demand Side Consulting
Energy Efficiency Consulting
Saving Clients Money
Helping Them Go "Green"
Managing Their Energy Requirements
Basically the goal for our company is to find the best procurement solution for our clients and reduce their energy consumption. This reduces their expenses and the amount of greenhouse gas they produce on a daily basis.
I have been in the energy footprint for the last 20 years and know that most companies are looking to "do whatever is necessary to get them to sign on the dotted line". I would prefer to walk away from a client that I can't help than to put them into a situation that they will regret for years to come. This is where the "TIDAL" part of the company name comes from.
The following is a catch phrase that encompasses what we do.
"Reducing your carbon footprint & energy bill at the same time!"
The back of the card needs to have this statement along with some sort of illustration. The back is a playground for creative ideas.
The front of the card needs the following.
Logo.
First & Last Name (Gus Marwick)
Title (Energy Warrior)
Phone Number (555) 314-2768
Fax Number (555) 862-4091
Email Address gus@tidalprimevoltage.example
Address 47 Orchard Lane Toronto Ontario K4P 2Z7
I want it to be a card that is remembered when any of my staff give it to a customer. It HAS to stand out.
Target Market(s)
Business Owners, Decision Makers, 30 to 65+
Industry/Entity Type
Business
Look and feel
Each slider illustrates characteristics of the customer's brand and the style your logo design should communicate.

```html
<!DOCTYPE html>
<html lang="en">
<head>
<meta charset="UTF-8">
<title>Tidal Prime Voltage Collective — Business Card</title>
<link rel="stylesheet" href="https://fonts.googleapis.com/css2?family=Exo+2:wght@500;600;700&family=Oswald:wght@500;600;700&display=swap">
<style>
  :root {
    --backdrop: #e9e6e1;
    --card: #ffffff;
    --ink: #1a1a1a;
    --grey: #6b6b6b;
    --green: #1fa84a;
    --green-dark: #1b5e2a;
    --blue: #3a6db5;
    --rule: #a9bddb;
    --illustration-from: #d9efe0;
    --illustration-to: #eef4ee;
  }
  * { box-sizing: border-box; margin: 0; padding: 0; }
  html, body {
    width: 1200px;
    height: 900px;
    overflow: hidden;
    background: var(--backdrop);
  }
  .canvas {
    position: relative;
    width: 1200px;
    height: 900px;
    display: flex;
    align-items: center;
    justify-content: center;
    gap: 40px;
  }
  .card {
    position: relative;
    width: 540px;
    height: 308px;
    background: var(--card);
    box-shadow: 0 6px 18px rgba(0, 0, 0, 0.14);
    overflow: hidden;
  }

  /* Back side */
  .card-back .tagline {
    position: absolute;
    left: 28px;
    top: 24px;
    width: 490px;
    font-family: "Oswald", sans-serif;
    font-weight: 600;
    font-size: 23px;
    line-height: 1.18;
    letter-spacing: 0.06em;
    color: var(--ink);
    text-transform: uppercase;
  }
  .tagline .quote-mark { color: var(--green); }
  .tagline .word-carbon { color: var(--grey); }
  .tagline .word-energy { color: var(--green); }
  .card-back .illustration {
    position: absolute;
    left: 28px;
    top: 104px;
    width: 484px;
    height: 134px;
    background: linear-gradient(90deg, var(--illustration-from), var(--illustration-to));
  }
  .card-back .brand-mini {
    position: absolute;
    right: 28px;
    bottom: 26px;
    display: flex;
    align-items: center;
    gap: 7px;
    font-family: "Exo 2", sans-serif;
    font-weight: 700;
    font-size: 14px;
    color: var(--blue);
  }
  .brand-dot {
    display: inline-block;
    border-radius: 50%;
    background: var(--green);
  }
  .brand-mini .brand-dot { width: 12px; height: 12px; }

  /* Front side */
  .card-front .brand {
    position: absolute;
    left: 0;
    right: 0;
    top: 66px;
    display: flex;
    align-items: center;
    justify-content: center;
    gap: 12px;
    font-family: "Exo 2", sans-serif;
    font-weight: 700;
    font-size: 25px;
    color: var(--blue);
  }
  .card-front .brand .brand-dot { width: 22px; height: 22px; }
  .card-front .brand-rule {
    position: absolute;
    left: 40px;
    right: 60px;
    top: 112px;
    height: 1px;
    background: var(--rule);
  }
  .contact-list {
    position: absolute;
    left: 40px;
    top: 132px;
    font-family: "Exo 2", sans-serif;
    font-weight: 600;
    font-size: 14px;
    letter-spacing: 0.04em;
    color: var(--ink);
  }
  .contact-row {
    display: flex;
    gap: 44px;
    margin-bottom: 12px;
  }
  .contact-item {
    display: flex;
    align-items: center;
    gap: 10px;
  }
  .contact-item svg { flex: none; }
  .contact-email { text-transform: uppercase; }
  .address {
    position: absolute;
    left: 22px;
    bottom: 30px;
    font-family: "Exo 2", sans-serif;
    font-weight: 700;
    font-size: 11.5px;
    letter-spacing: 0.03em;
    color: var(--green-dark);
    text-transform: uppercase;
  }
  .holder {
    position: absolute;
    right: 30px;
    bottom: 22px;
    text-align: right;
    font-family: "Oswald", sans-serif;
    color: var(--ink);
    text-transform: uppercase;
  }
  .holder-name {
    font-weight: 700;
    font-size: 21px;
    letter-spacing: 0.06em;
    line-height: 1;
  }
  .holder-title {
    font-weight: 500;
    font-size: 9px;
    letter-spacing: 0.08em;
  }
</style>
</head>
<body>
<main class="canvas">

  <section class="card card-back" aria-label="Card back">
    <p class="tagline">
      <span class="quote-mark">“</span>Reducing your <span class="word-carbon">carbon</span> footprint &amp;
      <span class="word-energy">energy</span> bill at the same time!<span class="quote-mark">”</span>
    </p>
    <div class="illustration" role="img" aria-label="Illustration of footprints turning from black to green and ending in green dollar signs"></div>
    <div class="brand-mini">
      <span class="brand-dot"></span>
      <span>TidalPrimeVoltageCollective</span>
    </div>
  </section>

  <section class="card card-front" aria-label="Card front">
    <div class="brand">
      <span class="brand-dot"></span>
      <span>TidalPrimeVoltageCollective</span>
    </div>
    <div class="brand-rule"></div>

    <div class="contact-list">
      <div class="contact-row">
        <span class="contact-item">
          <svg width="11" height="16" viewBox="0 0 11 16" aria-hidden="true">
            <rect x="1" y="1" width="9" height="14" rx="1.5" fill="none" stroke="var(--green)" stroke-width="1.6"/>
            <rect x="3" y="3" width="5" height="4" fill="var(--green)"/>
            <circle cx="5.5" cy="12" r="1" fill="var(--green)"/>
          </svg>
          (555) 314-2768
        </span>
        <span class="contact-item">
          <svg width="18" height="15" viewBox="0 0 18 15" aria-hidden="true">
            <rect x="4" y="0.5" width="10" height="4" fill="var(--green)"/>
            <rect x="0.5" y="4.5" width="17" height="7" rx="1.5" fill="var(--green)"/>
            <rect x="4" y="9" width="10" height="5.5" fill="#fff" stroke="var(--green)" stroke-width="1.2"/>
          </svg>
          (555) 862-4091
        </span>
      </div>
      <div class="contact-row">
        <span class="contact-item contact-email">
          <svg width="14" height="11" viewBox="0 0 14 11" aria-hidden="true">
            <rect x="0.8" y="0.8" width="12.4" height="9.4" fill="none" stroke="var(--green)" stroke-width="1.5"/>
            <path d="M1 1 L7 6 L13 1" fill="none" stroke="var(--green)" stroke-width="1.5"/>
          </svg>
          gus@tidalprimevoltage.example
        </span>
      </div>
    </div>

    <p class="address">47 Orchard Lane Toronto Ontario K4P 2Z7</p>
    <div class="holder">
      <p class="holder-name">Gus Marwick</p>
      <p class="holder-title">Energy Warrior</p>
    </div>
  </section>

</main>
</body>
</html>
```